GLOW LEAP TWIRL II (POSTCARD DESIGN)

Hello our original designer is no longer on this platform. We want to use design #51936074 with some minor adjustments. I've uploaded the original project 1) change the date on the front of card (keeping the same format) to August 27 with a start time of 2:30 PM.
2) on the front part of the card I want to include a splash graphic that says Back By Popular Demand! 3) replace pictures on the front with the attached photo. make it blend in. 3) Use the same photo on the back of the card.
Let the post card examples serve as template examples and let your creativity flourish! This is time sensitive so get these to me fast! If you're early you may win. thx

```html
<!DOCTYPE html>
<html lang="en">
<head>
<meta charset="utf-8">
<title>Glow Leap Twirl – Postcard Front</title>
<link rel="stylesheet" href="https://fonts.googleapis.com/css2?family=Montserrat:ital,wght@0,300;0,400;0,600;0,700;0,800;0,900;1,800;1,900&display=swap">
<style>
  :root {
    --page: #1a1a24;
    --navy: #12104a;
    --navy-deep: #0b0a33;
    --panel: #26357f;
    --pink: #e5226f;
    --teal: #35c3c9;
    --blue: #1f6fc4;
    --violet: #8d4fd1;
    --splash: #9b5cc9;
    --white: #ffffff;
    --gold: #f6c21c;
    --pill: #2477b8;
  }
  * { box-sizing: border-box; margin: 0; padding: 0; }
  html, body { width: 1200px; height: 864px; overflow: hidden; background: var(--page); }
  body { position: relative; font-family: "Montserrat", sans-serif; }

  .postcard {
    position: absolute; left: 0; top: 31px; width: 1200px; height: 802px; overflow: hidden;
    background: radial-gradient(ellipse at 35% 55%, #1c1a63 0%, var(--navy) 45%, var(--navy-deep) 100%);
  }
  .streaks { position: absolute; inset: 0; }

  .presenter {
    position: absolute; left: 51px; top: 44px;
    color: var(--pink); font-weight: 400; font-size: 25px; letter-spacing: 1.5px; line-height: 34px;
  }

  .title { position: absolute; left: 51px; font-style: italic; font-weight: 900; color: var(--white); letter-spacing: 1px; line-height: 1; }
  .title-line1 { top: 126px; font-size: 80px; }
  .title-line2 { top: 202px; font-size: 80px; }
  .title-line3 {
    top: 278px; font-size: 138px; letter-spacing: 4px;
    background: linear-gradient(90deg, var(--blue) 0%, var(--teal) 38%, var(--violet) 68%, var(--pink) 88%);
    -webkit-background-clip: text; background-clip: text; color: transparent;
  }

  .splash { position: absolute; left: 585px; top: 95px; width: 170px; height: 150px; }
  .splash-text {
    position: absolute; left: 612px; top: 132px; width: 120px; transform: rotate(-22deg);
    color: var(--white); font-weight: 800; font-size: 17px; line-height: 19px; text-align: center; text-transform: uppercase;
  }

  .date-day { position: absolute; left: 50px; top: 424px; font-size: 98px; font-weight: 700; color: var(--teal); line-height: 1; letter-spacing: -2px; }
  .date-month { position: absolute; left: 172px; top: 434px; font-size: 38px; font-weight: 700; color: var(--white); line-height: 1; letter-spacing: 1px; }
  .date-year { position: absolute; left: 166px; top: 468px; font-size: 54px; font-weight: 900; font-style: italic; color: var(--white); line-height: 1; }
  .date-divider { position: absolute; left: 363px; top: 436px; width: 3px; height: 86px; background: var(--pink); }
  .start-label { position: absolute; left: 390px; top: 436px; font-size: 31px; font-weight: 400; color: var(--white); letter-spacing: 1px; line-height: 1; }
  .start-time { position: absolute; left: 390px; top: 472px; font-size: 54px; font-weight: 600; color: var(--white); letter-spacing: 2px; line-height: 1; }

  .venue-pin { position: absolute; left: 50px; top: 543px; width: 30px; height: 38px; }
  .venue-name { position: absolute; left: 90px; top: 542px; font-size: 32px; font-weight: 400; color: var(--white); letter-spacing: 1.5px; line-height: 1; }
  .venue-city { position: absolute; left: 90px; top: 581px; font-size: 28px; font-weight: 400; color: var(--white); letter-spacing: 1px; line-height: 1; }

  .tickets-block {
    position: absolute; left: 52px; top: 652px; width: 176px; height: 108px;
    background: var(--panel); border-radius: 6px;
    display: flex; align-items: center; padding-left: 16px;
    font-size: 20px; font-weight: 700; color: var(--gold); line-height: 25px;
  }
  .box-office { position: absolute; left: 243px; top: 662px; font-size: 23px; font-weight: 700; color: var(--white); line-height: 1; }
  .box-phone { position: absolute; left: 243px; top: 690px; font-size: 29px; font-weight: 900; font-style: italic; color: var(--pink); line-height: 1; }
  .ticket-url {
    position: absolute; left: 243px; top: 724px; width: 358px; height: 40px; border-radius: 0 20px 20px 0;
    background: var(--pill); color: var(--white); font-weight: 700; font-size: 22px; letter-spacing: 3px;
    padding-left: 14px; line-height: 40px;
  }

  .portrait {
    position: absolute; left: 768px; top: 0; width: 432px; height: 802px;
    background:
      radial-gradient(ellipse 38% 22% at 48% 22%, rgba(120,80,70,0.9) 0%, rgba(60,30,40,0.0) 100%),
      radial-gradient(ellipse 60% 50% at 50% 68%, rgba(245,240,248,0.95) 0%, rgba(230,220,240,0.7) 55%, rgba(230,220,240,0) 80%),
      linear-gradient(180deg, rgba(18,16,74,0) 0%, rgba(150,170,210,0.35) 100%);
  }
</style>
</head>
<body>
  <main class="postcard">
    <svg class="streaks" width="1200" height="802" viewBox="0 0 1200 802" aria-hidden="true">
      <g stroke-linecap="round">
        <line x1="0" y1="130" x2="120" y2="30" stroke="#3f4fd6" stroke-width="3" opacity="0.6"/>
        <line x1="0" y1="190" x2="90" y2="110" stroke="#e5226f" stroke-width="2" opacity="0.4"/>
        <line x1="1060" y1="230" x2="1200" y2="60" stroke="#4a7ff0" stroke-width="14" opacity="0.55"/>
        <line x1="1080" y1="260" x2="1200" y2="120" stroke="#c96cf2" stroke-width="6" opacity="0.7"/>
        <line x1="1100" y1="360" x2="1200" y2="230" stroke="#e5226f" stroke-width="16" opacity="0.7"/>
        <line x1="1120" y1="420" x2="1200" y2="320" stroke="#ff3d6f" stroke-width="5" opacity="0.8"/>
        <line x1="900" y1="620" x2="1200" y2="820" stroke="#b070ff" stroke-width="3" opacity="0.5"/>
        <line x1="1150" y1="560" x2="1200" y2="700" stroke="#e5226f" stroke-width="3" opacity="0.6"/>
      </g>
    </svg>

    <div class="portrait" role="img" aria-label="Photo of the performer in a white blazer and jeans, hand at chin, blended into the background"></div>

    <p class="presenter">BRIGHTSTEP PRODUCTIONS PRESENTS<br>NORA JEAN WAVERLY’S</p>

    <h1>
      <span class="title title-line1">GLOW</span>
      <span class="title title-line2">LEAP</span>
      <span class="title title-line3">TWIRL</span>
    </h1>

    <svg class="splash" viewBox="0 0 170 150" aria-hidden="true">
      <circle cx="85" cy="78" r="62" fill="var(--splash)"/>
    </svg>
    <p class="splash-text">Back by popular demand!</p>

    <p class="date-day">27</p>
    <p class="date-month">AUGUST</p>
    <p class="date-year">2023</p>
    <div class="date-divider"></div>
    <p class="start-label">Start at</p>
    <p class="start-time">2:30 PM</p>

    <svg class="venue-pin" viewBox="0 0 30 38" aria-hidden="true">
      <path d="M15 1C7.3 1 2 6.6 2 13.6 2 23 15 33 15 33S28 23 28 13.6C28 6.6 22.7 1 15 1Z" fill="var(--pink)"/>
      <circle cx="15" cy="13.5" r="5" fill="var(--navy)"/>
      <ellipse cx="15" cy="35" rx="12" ry="2.5" fill="none" stroke="var(--pink)" stroke-width="2"/>
    </svg>
    <p class="venue-name">HARLOW PINES THEATRE</p>
    <p class="venue-city">Cedar Falls, CA</p>

    <p class="tickets-block">Buy<br>Tickets</p>

    <p class="box-office">Box Office</p>
    <p class="box-phone">(555) 210-SHOW</p>
    <p class="ticket-url">www.tix.example/gltw</p>
  </main>
</body>
</html>
```